Unique Concept Design to Website Needed

Please see the attached folder. I have random images,etc but most importantly I have an attached image I was working on as a concept of a website. The brown background with blue and brown squares. logo in upper left and a little about me and then the squares would have names on them to lead to a section of the website with more info. I envision, when you mouse over a square, an image would appear so I attached random images here as well. Maybe some squares already have some images too.
- I want simple fonts. i like CLEAN, fonts
- text should be minimal. i am changing my site to less text, more powerful, bolder, larger lines with less content
- i am not sold on brown as the secondary color. i like blue but maybe grays, whites, offwhite scales or some other colors
-i have another graphic in there too
-you can see from my mock what company i am. please feel free to look me up and pull any portfolio , info , etc content to help make a great mock.
Do something cool!

```html
<!DOCTYPE html>
<html lang="en">
<head>
<meta charset="utf-8">
<title>Company Name — Home</title>
<link rel="stylesheet" href="https://fonts.googleapis.com/css2?family=Fira+Sans:wght@300;600&display=swap">
<style>
  :root {
    --bg-center: #eef4f8;
    --bg-edge: #abc9d8;
    --navy: #02527a;
    --slate: #3d6a80;
    --azure: #03abff;
    --sky: #4dc1ff;
    --white: #ffffff;
    --tile-w: 188px;
    --tile-h: 147px;
  }
  * { box-sizing: border-box; margin: 0; padding: 0; }
  html, body { width: 1200px; height: 960px; overflow: hidden; }
  body {
    position: relative;
    font-family: "Fira Sans", "Helvetica Neue", Arial, sans-serif;
    background: radial-gradient(ellipse 620px 560px at 640px 560px, var(--bg-center) 0%, var(--bg-edge) 100%);
  }

  .brand {
    position: absolute;
    left: 20px;
    top: 36px;
    width: 160px;
    display: flex;
    flex-direction: column;
    align-items: center;
    color: var(--white);
  }
  .brand-dot {
    width: 100px;
    height: 100px;
    border: 7px solid var(--white);
    border-radius: 50%;
  }
  .brand-name {
    margin-top: 36px;
    font-weight: 600;
    font-size: 26px;
    line-height: 37px;
    text-align: center;
    letter-spacing: 0.2px;
  }

  .nav-grid { position: absolute; inset: 0; }
  .tile {
    position: absolute;
    width: var(--tile-w);
    height: var(--tile-h);
    display: flex;
    align-items: center;
    justify-content: center;
    text-align: center;
    color: var(--white);
    font-weight: 300;
    font-size: 30px;
    line-height: 42px;
    text-decoration: none;
  }
  .tile--navy { background: var(--navy); }
  .tile--slate { background: var(--slate); }
  .tile--azure { background: var(--azure); }
  .tile--sky { background: var(--sky); }
  .tile--testimonials { font-size: 27px; }

  .round-tl { border-top-left-radius: 46px; }
  .round-tr { border-top-right-radius: 46px; }
  .round-br { border-bottom-right-radius: 46px; }
  .round-bl { border-bottom-left-radius: 46px; }

  .corner {
    position: absolute;
    width: 36px;
    height: 36px;
    border: 0 solid var(--white);
  }
  .corner--tl { top: 6px; left: 6px; border-top-width: 1.5px; border-left-width: 1.5px; }
  .corner--tr { top: 6px; right: 6px; border-top-width: 1.5px; border-right-width: 1.5px; }
  .corner--bl { bottom: 6px; left: 6px; border-bottom-width: 1.5px; border-left-width: 1.5px; }
  .corner--br { bottom: 6px; right: 6px; border-bottom-width: 1.5px; border-right-width: 1.5px; }
</style>
</head>
<body>
  <header class="brand">
    <span class="brand-dot" aria-hidden="true"></span>
    <div class="brand-name">COMPANY<br>NAME</div>
  </header>

  <nav class="nav-grid" aria-label="Site sections">
    <a class="tile tile--navy round-tl" href="#about" style="left:253px; top:142px;">
      <span class="corner corner--tr"></span><span class="corner corner--bl"></span>About
    </a>

    <div class="tile tile--azure" style="left:253px; top:299px;"></div>
    <div class="tile tile--slate" style="left:451px; top:299px;"></div>
    <a class="tile tile--sky tile--testimonials round-tr" href="#testimonials" style="left:650px; top:299px;">
      <span class="corner corner--tl"></span><span class="corner corner--br"></span>Testimonials
    </a>

    <a class="tile tile--slate" href="#portfolio" style="left:253px; top:457px;">
      <span class="corner corner--tl"></span><span class="corner corner--br"></span>Portfolio
    </a>
    <div class="tile tile--navy" style="left:451px; top:457px;"></div>
    <div class="tile tile--azure" style="left:650px; top:457px;"></div>
    <a class="tile tile--navy round-br" href="#web-promo" style="left:848px; top:457px;">
      <span class="corner corner--tr"></span><span class="corner corner--bl"></span>Web<br>Promo
    </a>

    <a class="tile tile--sky round-bl" href="#media" style="left:451px; top:614px;">
      <span class="corner corner--tl"></span><span class="corner corner--br"></span>Media
    </a>
  </nav>
</body>
</html>
```